Label Design For My Pet Supplements Brand - Probiotic Dog Chews

Good Afternoon!
I am looking for a revamp of our current label design for my Probiotic Dog Chews. Attached is our current label and a mockup as well. I do like and appreciate our current design, but it lacks character, and appears to be really similar to other brands out there. I would like for the new label to take all the great characteristics of this label, but elevate them.
For context, our product is a 10oz White Jar with a White Lid.
I am attaching a full comprehensive guide that includes our existing files, fonts, .ai files, mockups, and our Brand Strategy. That way you're able to get an idea of what it is we sell and who exactly our customer is too. And that way we are able to create a label that speaks to our exact ideal customer. I am also supplying to you all the details for the label as well.
If you have any questions for me, feel free to ask. I'm looking forward to seeing your work!

```html
<!DOCTYPE html>
<html lang="en">
<head>
<meta charset="UTF-8">
<title>Barkle Probiotic Chews Label</title>
<link rel="stylesheet" href="https://fonts.googleapis.com/css2?family=Luckiest+Guy&family=Bebas+Neue&family=Montserrat:wght@500;800&display=swap">
<style>
  :root {
    --teal: #6cc7b8;
    --teal-deep: #3a9f90;
    --teal-shadow: #2f9a8a;
    --violet: #5a5ce0;
    --violet-deep: #4446d6;
    --orange: #ec9560;
    --orange-deep: #d9672a;
    --cream: #f4f0e8;
    --white: #ffffff;
  }
  * { margin: 0; padding: 0; box-sizing: border-box; }
  html, body { width: 1200px; height: 818px; overflow: hidden; background: var(--white); }
  .label {
    position: relative;
    width: 1200px;
    height: 818px;
    overflow: hidden;
  }
  .label-bands { position: absolute; inset: 0; }
  .flavor-badge {
    position: absolute;
    left: 140px;
    top: 0;
    width: 174px;
    height: 252px;
    background: linear-gradient(90deg, var(--violet-deep), var(--violet));
    border-radius: 0 0 87px 87px;
    text-align: center;
    padding-top: 30px;
  }
  .flavor-name {
    font-family: "Bebas Neue", sans-serif;
    font-size: 34px;
    line-height: 0.95;
    color: var(--cream);
    letter-spacing: 0.5px;
  }
  .flavor-art {
    width: 116px;
    height: 100px;
    margin: 18px auto 0;
    border-radius: 18px;
    background: linear-gradient(135deg, #f6a53c, #e0701d);
  }
  .brand-name {
    position: absolute;
    top: 52px;
    left: 0;
    right: 0;
    text-align: center;
    font-family: "Luckiest Guy", sans-serif;
    font-size: 100px;
    color: var(--cream);
    letter-spacing: 2px;
  }
  .product-title {
    position: absolute;
    top: 270px;
    left: 0;
    right: 0;
    text-align: center;
    font-family: "Luckiest Guy", sans-serif;
    color: var(--white);
    line-height: 1;
    text-shadow: 6px 6px 0 var(--teal-shadow);
  }
  .product-title .line-one { display: block; font-size: 150px; letter-spacing: 3px; transform: rotate(3deg); }
  .product-title .line-two { display: block; font-size: 140px; letter-spacing: 3px; margin-top: 14px; transform: rotate(-3deg); }
  .product-facts {
    position: absolute;
    top: 742px;
    left: 0;
    right: 0;
    display: flex;
    justify-content: center;
    align-items: center;
    gap: 22px;
    font-family: "Montserrat", sans-serif;
    font-weight: 500;
    font-size: 22px;
    color: var(--white);
    letter-spacing: 0.5px;
  }
  .product-facts .divider { width: 2px; height: 40px; background: var(--white); }
  .product-facts .count { font-weight: 800; font-size: 30px; letter-spacing: 1px; }
</style>
</head>
<body>
  <main class="label">
    <svg class="label-bands" width="1200" height="818" viewBox="0 0 1200 818" aria-hidden="true">
      <defs>
        <linearGradient id="orangeShade" x1="0" x2="1" y1="0" y2="0">
          <stop offset="0" stop-color="#d2580f"/>
          <stop offset="0.35" stop-color="#e2773a"/>
          <stop offset="1" stop-color="#f2a06c"/>
        </linearGradient>
        <linearGradient id="tealShade" x1="0" x2="1" y1="0" y2="0">
          <stop offset="0" stop-color="#1b8d7c"/>
          <stop offset="0.35" stop-color="#6ac5b6"/>
          <stop offset="1" stop-color="#78cdbf"/>
        </linearGradient>
      </defs>
      <rect width="1200" height="818" fill="url(#orangeShade)"/>
      <path d="M0 0 H1200 V470 Q600 960 0 470 Z" fill="var(--violet)"/>
      <path d="M0 0 H1200 V440 Q600 940 0 440 Z" fill="url(#tealShade)"/>
    </svg>

    <div class="flavor-badge">
      <p class="flavor-name">Peanut Butter<br>Flavor</p>
      <div class="flavor-art" role="img" aria-label="Illustration of peanut butter chew cubes"></div>
    </div>

    <h2 class="brand-name">BARKLE</h2>

    <h1 class="product-title">
      <span class="line-one">PROBIOTIC</span>
      <span class="line-two">CHEWS</span>
    </h1>

    <p class="product-facts">
      <span>SUPPLEMENT FOR DOGS</span>
      <span class="divider"></span>
      <span class="count">140 CT.</span>
      <span class="divider"></span>
      <span>NET CONTENTS 10 OZ.</span>
    </p>
  </main>
</body>
</html>
```